Brookmere Joinery Design Upgrade

- This is for a layout design of the home page only. No coding required.

- The design should be based around the attached HPID (home page information design) I've attached both a JPEG of this
- Information only is in RED text. Copy to go on the design in BLACK text. Some instructions are in the HPID. Please be creative!
- The design needs to be clean and spacious
- Use the logo provided. Please use the colours from the logos in the website design.
- I've attached some images to use as examples to use for home page gallery
- The product logos (Fenwyk, Clearbirch etc) showed in the HPV can be googled for a higher quality image if required.
- The header can be changed/altered - just needs to have all information as per logo, along with the phone number.

- Expected standard of design examples: (Please DO NOT copy these exactly – they are just examples)
http://www.palomir-works.co.nz/
http://www.hushlinecorp.co.nz/
http://www.dunkettle.co.nz/

Width of content will be 1100 pixels when implemented as a web page. Header height (without nav bar) 150-160 pixels.

The winning PSD file will have to be provided as follows…
1. Canvas size of 2000px x 2000px - 72ppi in Adobe Photoshop (CS5 compatible)
2. Width of content section is 1100px wide - centered in the canvas
3. Any button rollovers/hovers in the PSD as hidden layers.
4. All fonts used must be Google fonts (except for the header fonts).
5. You will need to supply the chosen home page plus one example page (example page as a style guide for how all other pages will look). Example page is only the header and navigational bar at the top, an empty sector in the middle with a column (180 px wide) which can be left or right aligned which means the main sector is 920 pixels wide, and then the footer at the bottom of the page.

```html
<!DOCTYPE html>
<html lang="en">
<head>
<meta charset="utf-8">
<title>Brookmere Joinery</title>
<link href="https://fonts.googleapis.com/css2?family=Open+Sans:wght@300;400;600;700&family=Oswald:wght@600&display=swap" rel="stylesheet">
<style>
:root{
  --header-bg:#272727;
  --nav-bg:#3a3f47;
  --card-head:#343941;
  --red:#e8141b;
  --yellow:#fff200;
  --text:#333;
  --muted:#555;
  --line:#d8d8d8;
  --footer-bg:#c3c4c6;
  --footer-text:#4a4f57;
  --bottom-bg:#343941;
  --gold:#c99a1e;
}
*{box-sizing:border-box;margin:0;padding:0}
html,body{width:1200px;height:1102px;overflow:hidden;background:#fff}
body{position:relative;font-family:"Open Sans",sans-serif;color:var(--text)}
.abs{position:absolute}
.site-header{left:0;top:0;width:1200px;height:88px;background:var(--header-bg)}
.brand{left:270px;top:14px;display:flex;align-items:center;gap:12px}
.brand-name{font-family:"Oswald",sans-serif;font-weight:600;font-size:30px;color:#fff;line-height:1;width:168px}
.brand-mark{width:57px;height:65px;background:var(--red)}
.header-contact{left:560px;top:10px;width:197px;text-align:right;color:#fff;font-size:10.5px;line-height:13px}
.header-contact .phone{font-size:12.5px;font-weight:600;margin-top:7px}
.tagline{left:542px;top:66px;width:214px;height:9px;background:var(--red);color:#fff;font-size:6.5px;font-weight:700;letter-spacing:.6px;line-height:9px;text-align:center;text-transform:uppercase}
.partner-name{left:780px;top:28px;width:150px;text-align:center;font-family:"Oswald",sans-serif;font-weight:600;font-size:26px;color:#fff;letter-spacing:2px}
.main-nav{left:0;top:88px;width:1200px;height:30px;background:var(--nav-bg)}
.main-nav ul{list-style:none;display:flex;justify-content:center;gap:13px;padding-top:9px}
.main-nav a{color:#fff;text-decoration:none;font-size:8.8px;text-transform:uppercase}
.page-title{left:269px;top:136px;font-weight:300;font-size:16px;color:#3c4047}
.hero{left:270px;top:176px;width:660px;height:280px;background:linear-gradient(180deg,#b9cde6 0%,#d9e1ea 30%,#e9e8e4 55%,#b9b5ac 72%,#6f8a3c 82%,#53702a 100%);border:1px solid #ccc}
.hero-caption{left:286px;top:402px;color:#fff;font-size:32px;font-weight:400}
.hero-shadow{left:280px;top:456px;width:640px;height:16px;background:radial-gradient(ellipse at top,rgba(0,0,0,.35),rgba(0,0,0,0) 70%)}
.quote-badge{left:841px;top:133px;width:90px;height:90px;border-radius:50%;background:var(--yellow);text-align:center;padding-top:28px;font-size:9.5px;line-height:12px;color:#2b2b2b}
.quote-badge strong{font-size:12px;font-weight:700;display:block}
.quote-badge .needs{font-weight:700}
.partners{left:270px;top:490px;width:660px;height:46px}
.partner{position:absolute;background:#b9babc}
.cards .card{position:absolute;border:1px solid var(--line);background:#fff;box-shadow:0 1px 2px rgba(0,0,0,.08)}
.card h2{height:27px;background:var(--card-head);color:#fff;font-size:11.5px;font-weight:600;padding:7px 11px}
.card p{font-family:Arial,sans-serif;font-size:8.2px;line-height:15px;color:#333;padding:0 10px;margin-top:15px}
.card p:first-of-type{margin-top:7px}
.site-footer{left:0;top:940px;width:1200px;height:134px;background:var(--footer-bg);color:var(--footer-text)}
.site-footer h3{font-size:11px;font-weight:600;text-transform:uppercase;color:#3c4047}
.footer-nav{left:291px;top:17px}
.footer-nav ul{list-style:none;columns:2;column-gap:16px;width:160px;margin-top:5px}
.footer-nav li{font-size:7.8px;line-height:10.8px}
.footer-divider{top:13px;width:1px;height:108px;background:#8a8d92}
.footer-contact{left:486px;top:17px;width:185px}
.footer-contact p{font-size:7.8px;line-height:10px;margin-top:5px}
.footer-contact p+p{margin-top:10px}
.guarantee{left:735px;top:15px;width:160px;text-align:center}
.guarantee-seal{width:72px;height:72px;border-radius:50%;background:var(--gold);margin:0 auto;border:4px solid #e2bc45}
.guarantee p{font-size:7.5px;line-height:10px;margin-top:9px;color:#333}
.bottom-bar{left:0;top:1074px;width:1200px;height:28px;background:var(--bottom-bg);color:#fff;font-size:7.8px}
.bottom-bar span{position:absolute;top:10px}
</style>
</head>
<body>
<header class="site-header abs">
  <div class="brand abs">
    <div class="brand-name">Brookmere Joinery</div>
    <div class="brand-mark"></div>
  </div>
  <div class="header-contact abs">
    <div>Kestrel Vale</div>
    <div>Harbourton</div>
    <div class="phone">(04) 555 0192</div>
  </div>
  <div class="tagline abs">Excellence in aluminium windows &amp; doors</div>
  <div class="partner-name abs">FENWYK</div>
</header>

<nav class="main-nav abs">
  <ul>
    <li><a href="#">Home</a></li><li><a href="#">About Us</a></li><li><a href="#">New Homes</a></li><li><a href="#">Commercial</a></li><li><a href="#">Replacement Joinery</a></li><li><a href="#">Double Glazing</a></li><li><a href="#">Conservatories</a></li><li><a href="#">Gallery</a></li><li><a href="#">Free Quote</a></li><li><a href="#">Contact</a></li>
  </ul>
</nav>

<h1 class="page-title abs">Ensuring Style and Functionality with Your Alumininum Joinery</h1>

<div class="hero abs" role="img" aria-label="Photo of a white commercial building with rows of aluminium bay windows behind a green hedge"></div>
<div class="hero-caption abs">Commercial Joinery</div>
<div class="hero-shadow abs"></div>

<div class="quote-badge abs"><strong>Get a FREE</strong>Quote for your<br><span class="needs">Joinery Needs</span></div>

<div class="partners abs" aria-label="Partner badges">
  <div class="partner" style="left:24px;top:5px;width:60px;height:36px;border-radius:2px"></div>
  <div class="partner" style="left:122px;top:2px;width:114px;height:38px;border-radius:50%"></div>
  <div class="partner" style="left:242px;top:3px;width:44px;height:38px"></div>
  <div class="partner" style="left:317px;top:-4px;width:50px;height:50px;border-radius:50%"></div>
  <div class="partner" style="left:390px;top:12px;width:104px;height:18px"></div>
  <div class="partner" style="left:513px;top:11px;width:118px;height:20px"></div>
</div>

<section class="cards">
  <article class="card" style="left:270px;top:572px;width:205px;height:178px">
    <h2>New Homes</h2>
    <p>Building your dream home?</p>
    <p>Brookmere Joinery can provide a wide range of stylish and functional options to help you get your dream home.</p>
    <p>From glass sliding doors to aluminium team will work closely with you to ensure you get the best result for your new home.</p>
  </article>
  <article class="card" style="left:498px;top:572px;width:205px;height:178px">
    <h2>Commercial</h2>
    <p>Building your dream home?</p>
    <p>Brookmere Joinery can provide a wide range of stylish and functional options to help you get your dream home.</p>
    <p>From glass sliding doors to aluminium team will work closely with you to ensure you get the best result for your new home.</p>
  </article>
  <article class="card" style="left:726px;top:572px;width:205px;height:178px">
    <h2>Replacement Joinery</h2>
    <p>Building your dream home?</p>
    <p>Brookmere Joinery can provide a wide range of stylish and functional options to help you get your dream home.</p>
    <p>From glass sliding doors to aluminium team will work closely with you to ensure you get the best result for your new home.</p>
  </article>
  <article class="card" style="left:270px;top:770px;width:319px;height:147px">
    <h2>Double Glazing</h2>
    <p>Building your dream home?</p>
    <p>Brookmere Joinery can provide a wide range of stylish and functional options to help you get your dream home.</p>
    <p>From glass sliding doors to aluminium team will work closely with you to ensure you get the best result for your new home.</p>
  </article>
  <article class="card" style="left:610px;top:770px;width:321px;height:147px">
    <h2>Conservatories</h2>
    <p>Building your dream home?</p>
    <p>Brookmere Joinery can provide a wide range of stylish and functional options to help you get your dream home.</p>
    <p>From glass sliding doors to aluminium team will work closely with you to ensure you get the best result for your new home.</p>
  </article>
</section>

<footer class="site-footer abs">
  <div class="footer-nav abs">
    <h3>Navigation</h3>
    <ul>
      <li>Home</li><li>About</li><li>Testimonials</li><li>New homes</li><li>Commercial</li><li>Replacement Joinery</li>
      <li>Double Glazing</li><li>Conservatories</li><li>Gallery</li><li>Free Quote</li><li>Contact</li>
    </ul>
  </div>
  <div class="footer-divider abs" style="left:463px"></div>
  <div class="footer-contact abs">
    <h3>Contact Details</h3>
    <p>Physical Address: 14 Larchfield Cres, Kestrel Vale</p>
    <p>Tel: +04 555 0192<br>Fax: +04 555 0193</p>
    <p>Postal Address: PO Box 70215, Kestrel Vale</p>
  </div>
  <div class="footer-divider abs" style="left:706px"></div>
  <div class="guarantee abs">
    <div class="guarantee-seal" role="img" aria-label="Money back guarantee seal"></div>
    <p>We guarantee all our work. If there is ever a problem, we will be back to provide a solution</p>
  </div>
</footer>

<div class="bottom-bar abs">
  <span style="left:270px">Copyright © 2014 Brookmere Joinery. All Rights Reserved.</span>
  <span style="right:270px">Website Design by northpixel.co.nz</span>
</div>
</body>
</html>
```